Face cream packaging | Cosmetic start-up

This project is about creating design proposals for two different types of packaging. Once to a cream jar made of glass and once to a jar made of plastic.
Three different designs must be created for each type of jar. Later, the different packaging will be used as customization options in an online store for cosmetics.

- The packaging variant made of glass should have color gradients. Three different shades are to be chosen. (Preferably with the primary colors red, blue and green). Note: The designer can create other proposals at will if he has better ideas. The logo must be included in some form. (Link to manufacturer description: https://catalogue.vorelpackwerk.com/en/portals/vorelpackwerk/assets/48302915/lio-50-ml/)

- With the plastic type of packaging, the designer has a lot of freedom to design. The only requirement is that the design must be artistic. It doesn't matter whether abstract patterns, geometric figures, mandalas or just a basic color is chosen. The main thing is that the packaging inspires. The logo must be included in some form. (Link to manufacturer description: https://catalogue.vorelpackwerk.com/en/portals/vorelpackwerk/assets/48302922/tova-50-ml/)

Thank you in advance for your work and best regards
Ubel

Target Market(s)

Young people with an affinity for social media and the web. Focus is on the female clientele.

Industry/Entity Type

Cosmetics

Font styles to use
Script

Colors
eea4c8
f59195
85cae6
cadf82

Requirements
Must have
• The logo must be included in some form. (PNG-File attached)
Nice to have
• Other types of packaging (can shape, packaging material)

```html
<!DOCTYPE html>
<html lang="en">
<head>
<meta charset="utf-8">
<title>noa cosmetics – night facial cream labels</title>
<link rel="stylesheet" href="https://fonts.googleapis.com/css2?family=Poppins:wght@300&family=Mali:wght@600&display=swap">
<style>
  :root {
    --canvas: #f6f8f7;
    --label: #ffffff;
    --ink: #2b2b2b;
    --rule: #3a3a3a;
    --band-text: #ffffff;
    --rose: #ee6fa8;
    --sky: #2f8fd6;
    --leaf: #45b33f;
    --floral-warm: #f2a23a;
    --floral-red: #e0503a;
    --floral-green: #7cb84a;
    --floral-teal: #4aa9a0;
  }
  * { box-sizing: border-box; margin: 0; padding: 0; }
  html, body { width: 1200px; height: 1200px; overflow: hidden; }
  body {
    background: var(--canvas);
    display: flex;
    align-items: center;
    justify-content: center;
    gap: 40px;
  }
  .label {
    position: relative;
    width: 350px;
    height: 200px;
    background: var(--label);
    overflow: hidden;
    box-shadow: 0 1px 3px rgba(0,0,0,0.08);
  }
  .color-band {
    position: absolute;
    left: 0; right: 0;
    top: 98px;
    height: 78px;
  }
  .label--rose .color-band { background: linear-gradient(90deg, var(--rose) 0%, var(--rose) 45%, rgba(238,111,168,0) 90%); }
  .label--sky  .color-band { background: linear-gradient(90deg, rgba(47,143,214,0) 8%, var(--sky) 40%, var(--sky) 100%); }
  .label--leaf .color-band { background: linear-gradient(90deg, rgba(69,179,63,0) 8%, var(--leaf) 40%, var(--leaf) 100%); }
  .floral {
    position: absolute;
    top: 14px;
    width: 78px;
    height: 172px;
    border-radius: 40px;
    background: radial-gradient(circle at 50% 40%, var(--floral-warm) 0%, var(--floral-red) 35%, var(--floral-green) 65%, var(--floral-teal) 100%);
    opacity: 0.85;
  }
  .floral--left { left: -30px; }
  .floral--right { right: -30px; }
  .brand {
    position: absolute;
    left: 86px;
    top: 22px;
    font-family: "Poppins", sans-serif;
    font-weight: 300;
    color: var(--ink);
    font-size: 30px;
    line-height: 1;
  }
  .brand-rule {
    position: absolute;
    left: 98px;
    top: 82px;
    width: 150px;
    height: 1px;
    background: var(--rule);
  }
  .product-name {
    position: absolute;
    left: 110px;
    top: 118px;
    font-family: "Mali", cursive;
    font-weight: 600;
    font-size: 15px;
    color: var(--band-text);
    letter-spacing: 0.5px;
  }
  .net-size {
    position: absolute;
    left: 110px;
    top: 156px;
    font-family: "Poppins", sans-serif;
    font-weight: 300;
    font-size: 9px;
    color: var(--band-text);
  }
</style>
</head>
<body>
  <section class="label label--rose">
    <div class="color-band"></div>
    <div class="floral floral--left" role="img" aria-label="Hand-drawn floral illustration of colourful blossoms and leaves"></div>
    <div class="floral floral--right" role="img" aria-label="Hand-drawn floral illustration of colourful blossoms and leaves"></div>
    <p class="brand">noa<br>cosmetics</p>
    <div class="brand-rule"></div>
    <p class="product-name">night facial cream</p>
    <p class="net-size">1/2 oz (14.79ml)</p>
  </section>

  <section class="label label--sky">
    <div class="color-band"></div>
    <div class="floral floral--left" role="img" aria-label="Hand-drawn floral illustration of colourful blossoms and leaves"></div>
    <div class="floral floral--right" role="img" aria-label="Hand-drawn floral illustration of colourful blossoms and leaves"></div>
    <p class="brand">noa<br>cosmetics</p>
    <div class="brand-rule"></div>
    <p class="product-name">night facial cream</p>
    <p class="net-size">1/2 oz (14.79ml)</p>
  </section>

  <section class="label label--leaf">
    <div class="color-band"></div>
    <div class="floral floral--left" role="img" aria-label="Hand-drawn floral illustration of colourful blossoms and leaves"></div>
    <div class="floral floral--right" role="img" aria-label="Hand-drawn floral illustration of colourful blossoms and leaves"></div>
    <p class="brand">noa<br>cosmetics</p>
    <div class="brand-rule"></div>
    <p class="product-name">night facial cream</p>
    <p class="net-size">1/2 oz (14.79ml)</p>
  </section>
</body>
</html>
```